Auction Company Wordpress Design Project

We need a WordPress design/concept for an established auctioneering company specializing in Benefit Auctions, Estate Auctions, Business Liquidations/Overstocks, and real estate marketing in the Chicago area. The winning design will have a professional look appealing to clients searching for these services.

Industry/Entity Type

Real Estate

Requirements
Must have
• - We will require winning designer to provide a layered PSD (Adobe photoshop) concept file, along with any non-standard font files used.

The site's navigation: 1) Home, 2) Auctions, 3) About Us, 4) Buyers, 5) Sellers, 6) Media, 7) Contact Us. Horizontal structure preferred.

A slideshow element will be represented (choice of files attached) preferably in the header. The following widgets will also be incorporated into sidebar (or other creative placement):
- Brightway Mailer email signup
- Featured Auctions (example shown in http://www.bidlantern-example.com/ as "Upcoming Auctions" widget)
- Vidora video widget
- Social media widget for Friendlyn, Chirpel, Vidora icons
- Testimonials widget

Winning design will creatively use colors in logo (with perhaps accent color) with a professional, clean look. Client mentions liking the use of color in http://www.plotgleam-example.com/

Footer of site will have generic contact info (phone number, email addresses, mailing address; a smaller instance of logo; and the attached association logos.
Nice to have
• - Use of drop-down menus should be demonstrated by incorporating mouse-over for 1) Upcoming, 2) Online, 3) Past, under the 'Auctions' main menu item (for clarity of design, this drop-down can be placed under any other menu item if necessary).
Should not have
• Please do not use auction gavels in the design.

```html
<!DOCTYPE html>
<html lang="en">
<head>
<meta charset="utf-8">
<title>Harborgate Auction Realty</title>
<link rel="stylesheet" href="https://fonts.googleapis.com/css2?family=Open+Sans:wght@400;600;700&family=Arimo:wght@400;700&display=swap">
<style>
:root{
  --sky:#2f9be0;
  --field:#7ea83a;
  --cream:#f7e7cd;
  --cream-line:#f2ddbd;
  --gold-hi:#eedcb0;
  --gold:#d8c28f;
  --gold-dark:#b9a473;
  --brown:#3e3019;
  --brown-2:#5a4528;
  --text:#3c3c3c;
  --muted:#555;
  --red:#e0241b;
  --rule:#d3d3d3;
  --olive:#8f8a1e;
}
*{box-sizing:border-box;margin:0;padding:0}
html,body{width:754px;height:1200px;overflow:hidden}
body{position:relative;font-family:"Arimo",Arial,sans-serif;color:var(--text);font-size:9px;line-height:1.45;
  background:linear-gradient(180deg,var(--sky) 0%,#6ab7e6 34%,#9bb78a 42%,var(--field) 60%,#b9c94a 100%)}
.backdrop{position:absolute;inset:0}
.page{position:absolute;left:34px;top:0;width:681px;height:1200px;background:#fff}
.abs{position:absolute}
/* header */
.header{left:0;top:0;width:681px;height:126px;border-top:4px solid #2b2b2b;
  background:repeating-linear-gradient(90deg,var(--cream) 0 6px,var(--cream-line) 6px 12px)}
.brand{left:14px;top:16px;width:130px;text-align:center;font-family:"Open Sans",sans-serif;font-weight:700;color:var(--brown-2)}
.brand-mark{display:block;width:26px;height:26px;margin:0 auto 6px;background:var(--gold-dark)}
.brand-name{font-size:27px;line-height:1;letter-spacing:.5px}
.brand-sub{font-size:11px;line-height:1.2;letter-spacing:.6px;margin-top:3px}
.phone{left:376px;top:10px;display:flex;align-items:center;gap:8px;font-family:"Open Sans",sans-serif;font-size:18px;color:#222}
.social-tab{left:524px;top:0;width:155px;height:34px;background:#2c2c2c;clip-path:polygon(0 0,100% 0,100% 100%,12% 100%);display:flex;gap:7px;align-items:center;justify-content:flex-end;padding-right:10px;color:#fff;font-size:8px;font-family:"Open Sans",sans-serif}
.social-tab span::before{content:"";display:inline-block;width:7px;height:7px;border-radius:50%;background:#6aa3d9;margin-right:3px;vertical-align:-1px}
.search{left:438px;top:86px;display:flex;height:25px}
.search-field{width:143px;border:1px solid #d7c9a8;background:#fff;color:#999;font-size:8px;padding:7px 7px}
.search-btn{width:63px;background:linear-gradient(var(--gold-hi),var(--gold-dark));font-family:"Open Sans",sans-serif;font-size:12px;color:#2e2410;text-align:center;line-height:25px}
/* nav */
.nav{left:0;top:126px;width:681px;height:37px;background:linear-gradient(var(--gold-hi),var(--gold));display:flex;list-style:none;font-family:"Arimo",sans-serif;font-size:9px;color:#1d1d1d}
.nav li{line-height:37px;flex:1;text-align:center}
.nav li.active{flex:0 0 80px;background:var(--brown);color:#fff}
/* slider */
.slider{left:11px;top:180px;width:658px;height:281px;border:1px solid #cfcfcf;padding:4px;box-shadow:0 1px 3px rgba(0,0,0,.2)}
.slide-photo{width:100%;height:100%;background:linear-gradient(180deg,#9fc4e6 0%,#c9d8e6 40%,#b9a98e 70%,#4d4a30 100%)}
.arrow{top:301px;width:16px;height:40px;background:#a3a51b}
.arrow.left{left:14px;border-radius:0 20px 20px 0}
.arrow.right{left:651px;border-radius:20px 0 0 20px}
/* sidebar */
.video{left:11px;top:470px;width:217px;height:149px;background:#000;color:#fff}
.video .replay{position:absolute;left:88px;top:57px;font-size:8px}
.video .bar{position:absolute;left:0;bottom:0;width:100%;height:9px;background:#ddd;font-size:6px;color:#333;padding-left:4px;line-height:9px}
.video .bar i{position:absolute;left:60px;top:4px;width:110px;height:2px;background:var(--red)}
.video .tag{position:absolute;right:8px;bottom:12px;font-size:7px;color:#555}
.card{left:11px;width:217px;border:1px solid #d4d4d4;box-shadow:0 1px 3px rgba(0,0,0,.15);background:#fff}
.card h3{font-family:"Open Sans",sans-serif;font-weight:600;font-size:12px;text-align:center;color:#222;margin-top:7px}
.auction-photo{width:198px;height:131px;margin:8px auto 0;border:1px solid #bbb;padding:3px}
.auction-photo div{width:100%;height:100%;background:linear-gradient(180deg,#6fb2e2 0%,#a8d0ef 40%,#4f7a33 58%,#b02d22 72%,#7aa547 100%)}
.lot{text-align:center;font-size:8.5px;font-weight:700;color:#222;margin-top:5px;line-height:1.5}
.lot em{font-style:normal;color:var(--red)}
.btn{display:block;margin:6px auto 0;width:197px;background:linear-gradient(var(--gold-hi),var(--gold-dark));border:1px solid #a8956a;text-align:center;font-family:"Open Sans",sans-serif;color:#2e2410}
.btn.big{height:32px;line-height:32px;font-size:12px}
.btn.small{height:25px;line-height:25px;font-size:11px;margin-top:8px}
.card p.note{font-size:8.5px;margin:8px 9px 0}
.share{left:15px;top:1009px;display:flex;gap:5px;align-items:center;font-size:8px}
.share span{border:1px solid #c5d0e0;background:#eef2f8;padding:1px 4px;color:#3b5998}
/* main */
.content{left:243px;width:427px}
.content h2{font-family:"Open Sans",sans-serif;font-weight:600;font-size:12.5px;color:#222;letter-spacing:.3px;border-bottom:2px solid var(--rule);padding-bottom:3px}
.content p{font-size:8.5px;line-height:1.48;margin-top:9px;padding:0 3px}
.points{list-style:none;font-weight:700;font-size:8.5px;margin:16px 0 0 20px}
.points li{margin-bottom:6px;padding-left:14px;position:relative}
.points li::before{content:"";position:absolute;left:0;top:3px;width:5px;height:5px;background:#444;transform:rotate(45deg)}
.testimonial{left:254px;top:829px;width:416px}
.testimonial h2{font-family:"Open Sans",sans-serif;font-weight:600;font-size:12.5px;color:#222;border-bottom:2px solid var(--rule);padding-bottom:4px}
.quote{position:relative;padding:8px 8px 0 30px;font-size:8.5px;line-height:1.45}
.quote p{margin-bottom:10px}
.qmark{position:absolute;font-family:Georgia,serif;font-size:34px;font-weight:700;color:#222;line-height:1}
.byline{margin-top:14px;border-top:2px solid var(--rule);padding-top:5px;display:flex;justify-content:space-between;font-size:8.5px;font-weight:700}
.byline span b,.byline a{color:var(--olive)}
.byline a{text-decoration:none}
/* footer */
.footer-nav{left:11px;top:1054px;width:658px;height:47px;background:var(--brown);color:#fff;font-size:9px;display:flex;align-items:center;padding-left:22px;gap:11px}
.badges{position:absolute;right:10px;top:6px;display:flex;gap:12px}
.badges i{width:34px;height:34px;background:#2a1f0e;border-radius:3px}
.offices{left:17px;top:1111px;width:650px;display:flex;font-size:8.5px;line-height:1.45;color:#222}
.office{width:166px}
.office b{font-weight:700}
.touch{margin-left:10px}
.touch b{font-weight:700}
.touch .icons{display:flex;gap:6px;margin-top:8px}
.touch .icons i{width:22px;height:22px;border-radius:50%;background:#5b82c4}
.touch .icons i:nth-child(2){background:#4cb3e6}
.touch .icons i:nth-child(3){background:#f08a25}
.touch .icons i:nth-child(4){background:#c9c9c9}
.copyright{left:0;top:1176px;width:681px;text-align:center;font-size:8px;color:#222;border-top:1px solid #e2e2e2;padding-top:5px;margin:0 11px;width:658px}
</style>
</head>
<body>
<div class="backdrop" role="img" aria-label="Full-width backdrop photo of blue sky over a farm field with red barns"></div>

<div class="page">
  <header class="abs header">
    <div class="abs brand">
      <span class="brand-mark"></span>
      <div class="brand-name">HARBORGATE</div>
      <div class="brand-sub">AUCTION REALTY</div>
    </div>
    <div class="abs phone">
      <svg width="20" height="20" viewBox="0 0 20 20"><circle cx="10" cy="10" r="9" fill="#c9a86a"/><path d="M7 5c1 0 1.5 2.5 1 3l-1 1c.8 1.6 1.8 2.6 3.2 3.2l1-1c.5-.5 3 0 3 1s-1 2.3-2.3 2.3C8 14.5 5.5 12 5.5 7.3 5.5 6 6 5 7 5z" fill="#fff"/></svg>
      <span>555.0142.880</span>
    </div>
    <div class="abs social-tab"><span>Friendlyn</span><span>Chirpel</span><span>Vidora</span></div>
    <div class="abs search">
      <div class="search-field">Type Keywords</div>
      <div class="search-btn">SEARCH</div>
    </div>
  </header>

  <ul class="abs nav">
    <li class="active">HOME</li><li>AUCTIONS</li><li>ABOUT US</li><li>BUYERS</li><li>SELLERS</li><li>MEDIA</li><li>CONTACT US</li>
  </ul>

  <div class="abs slider"><div class="slide-photo" role="img" aria-label="Slideshow photo of a lit two-storey suburban house at dusk with an auction sign on the lawn"></div></div>
  <div class="abs arrow left"></div>
  <div class="abs arrow right"></div>

  <div class="abs video" role="img" aria-label="Vidora video player">
    <span class="replay">⟲ Replay</span>
    <span class="tag">Vidora</span>
    <div class="bar">▶ ◂) 2:12/3:12<i></i></div>
  </div>

  <section class="abs card" style="top:631px;height:252px">
    <h3>UPCOMING AUCTIONS</h3>
    <div class="auction-photo"><div role="img" aria-label="Photo of a red barn with grain silos under a blue sky"></div></div>
    <div class="lot">SINGLE FAMILY HOME AUCTION<br>Original Price: <em>$6.1M – Sealed Bid Auction,<br>Jan. 7th – Published Reserve $3.8 M</em></div>
    <div class="btn big">MORE INFORMATION</div>
  </section>

  <section class="abs card" style="top:899px;height:97px">
    <h3>JOIN EMAIL LIST</h3>
    <p class="note">To stay informed about our services and upcoming events, please join our mailing list.</p>
    <div class="btn small">SUBSCRIBE</div>
  </section>

  <div class="abs share"><span>Friendlyn</span>2<span>Chirpel</span><span>7,231</span></div>

  <section class="abs content" style="top:470px">
    <h2>WELCOME TO HARBORGATE AUCTION REALTY</h2>
    <p>Lorem ipsum dolor sit amet, consectetur adipiscing elit. Pellentesque ut lobortis tortor. Nullam accumsan aliquam facilisis. Nullam ac erat viverra diam placerat mattis ut id elit. Ut a augue risus. Duis ut accumsan neque. Morbi iaculis sagittis neque eget venenatis. Etiam ultrices tortor ac metus faucibus viverra. Quisque id tortor est, vitae pharetra tortor.</p>
    <p style="margin-top:14px">Nulla luctus mauris congue nisl tristique auctor. Aenean suscipit, libero at suscipit molestie, nulla orci lobortis ligula, at tristique libero sem eu dolor. Aenean non mauris nisi. Nam lobortis feugiat mollis. Aenean sagittis, lacus sed fermentum ullamcorper, augue enim viverra risus, in fringilla quam mi vestibulum turpis. Integer et consectetur velit.</p>
    <ul class="points">
      <li>Sed non sem nec eros varius ullamcorper.</li>
      <li>Phasellus pulvinar felis nec sem ultrices posuere.</li>
      <li>In in libero sed neque pulvinar placerat in eleifend metus.</li>
      <li>Proin non lorem a purus porta ornare tincidunt non felis.</li>
      <li>Nullam eu odio neque, ut iaculis neque.</li>
    </ul>
    <p style="margin-top:18px">Cras pellentesque mauris et magna venenatis vitae vehicula eros scelerisque. Nulla eget luctus tellus. Donec ut quam ipsum, nec ultrices lacus. Pellentesque ultrices metus et tortor luctus rutrum. Etiam elementum augue quis justo consequat vitae ornare sapien tincidunt.Lorem ipsum dolor sit amet, consectetur adipiscing elit. Pellentesque ut lobortis tortor. Nullam accumsan aliquam facilisis. Nullam ac erat viverra diam placerat mattis ut id elit. Ut a augue risus. Duis ut accumsan neque. Morbi iaculis</p>
  </section>

  <section class="abs testimonial">
    <h2>WHAT CLIENT SAYS?</h2>
    <div class="quote">
      <span class="qmark" style="left:3px;top:6px">“</span>
      <p>Lorem ipsum dolor sit amet, consectetur adipiscing elit. Pellentesque ut lobortis tortor. Nullam accumsan aliquam facilisis. Nullam ac erat viverra diam placerat mattis ut id elit. Ut a augue risus. Duis ut accumsan neque. Morbi iaculis sagittis neque eget venenatis.</p>
      <p>Lorem ipsum dolor sit amet, consectetur adipiscing elit. Pellentesque ut lobortis tortor. Nullam accumsan aliquam facilisis. Nullam ac erat viverra diam placerat mattis ut id elit. Ut a augue risus. Duis ut accumsan neque. Morbi iaculis sagittis neque eget venenatis.</p>
      <span class="qmark" style="right:30px;bottom:-14px">”</span>
    </div>
    <div class="byline"><span>Owen Marlow, <b>CEO Fernbright Studio</b></span><a>More Testimonials</a></div>
  </section>

  <nav class="abs footer-nav">
    HOME <span>|</span> AUCTIONS <span>|</span> ABOUT US <span>|</span> BUYERS <span>|</span> SELLERS <span>|</span> MEDIA <span>|</span> CONTACT US
    <div class="badges"><i></i><i></i><i></i></div>
  </nav>

  <div class="abs offices">
    <div class="office"><b>Office 1</b><br>Phone: 555- 014-2210<br>Fax: 555- 014-7765<br>info@bidlantern-example.com</div>
    <div class="office"><b>Office 2</b><br>Phone: 555- 014-2210<br>Fax: 555- 014-7765<br>info@bidlantern-example.com</div>
    <div class="office"><b>Office 3</b><br>Phone: 555- 014-2210<br>Fax: 555- 014-7765<br>info@bidlantern-example.com</div>
    <div class="touch"><b>Get In Touch</b><div class="icons"><i></i><i></i><i></i><i></i></div></div>
  </div>

  <div class="abs copyright">© 2013, All Rights Reserved, Harborgate Auction Realty</div>
</div>
</body>
</html>
```